Halvorine Ledgers & Advisory Tri-Fold Brochure (8.5"x11")

I need a professional looking brochure for my bookkeeping business. I am looking for something professional yet casual (not too corporate looking). I have attached a sample brochure that will outline the areas and a copy of our logo. I'd like to stick with shades of blue. The final product should communicate professional and personal.

Target Market(s)

Small service businesses.

Industry/Entity Type

Business

Font styles to use
Sans Serif

Requirements
Must have
• Professional looking photos of people in areas where it asks for a picture.

```html
<!DOCTYPE html>
<html lang="en">
<head>
<meta charset="utf-8">
<title>Halvorine Ledgers &amp; Advisory – Tri-Fold Brochure</title>
<link rel="stylesheet" href="https://fonts.googleapis.com/css2?family=Noto+Serif:wght@400&family=Open+Sans:wght@400;600&display=swap">
<style>
  :root {
    --bg: #a9c9e2;
    --paper: #f2f3f5;
    --blue: #1e94d6;
    --blue-deep: #127ec0;
    --ink: #111418;
    --dark-rule: #1b2430;
    --photo-a: #e9e6e2;
    --photo-b: #7d8fa6;
    --photo-c: #1f2d45;
  }
  * { margin: 0; padding: 0; box-sizing: border-box; }
  html, body { width: 1200px; height: 1054px; overflow: hidden; background: var(--bg); }
  body { font-family: "Noto Serif", Georgia, serif; color: var(--ink); }

  .brochure {
    position: absolute; left: 30px; top: 97px;
    width: 1140px; height: 860px;
    background: var(--paper);
  }
  .brochure-art { position: absolute; inset: 0; }

  .panel { position: absolute; top: 0; width: 380px; height: 860px; }
  .panel-inside { left: 0; }
  .panel-back { left: 380px; }
  .panel-cover { left: 760px; }

  .headline { position: absolute; left: 28px; top: 272px; font-size: 27px; line-height: 1.08; font-weight: 400; }
  .section-title { position: absolute; left: 28px; display: flex; align-items: center; gap: 12px;
    color: var(--blue); font-size: 23px; }
  .what-title { top: 350px; }
  .talk-title { top: 700px; }
  .icon-dot { width: 30px; height: 30px; border-radius: 50%; background: var(--blue);
    display: flex; align-items: center; justify-content: center; }
  .about-copy { position: absolute; left: 28px; top: 398px; width: 338px;
    font-size: 15.2px; line-height: 1.13; text-align: justify; }
  .talk-copy { position: absolute; left: 28px; top: 746px; width: 340px; font-size: 17px; line-height: 1.2; }

  .values { position: absolute; left: 18px; top: 52px; list-style: none; }
  .values li { display: flex; align-items: center; gap: 20px; height: 63px; font-size: 26px; }

  .contact { position: absolute; left: 30px; top: 676px; font-size: 17px; line-height: 1.22; }
  .contact-title { color: var(--blue); font-size: 17px; }
  .back-brand { position: absolute; left: 30px; top: 800px; font-size: 17px; color: var(--blue-deep); }
  .back-address { position: absolute; left: 168px; top: 790px; font-size: 16px; line-height: 1.1; text-transform: uppercase; }

  .cover-mark { position: absolute; left: 62px; top: 245px; width: 246px; height: 246px;
    background: rgba(255,255,255,0.28); display: flex; align-items: center; justify-content: center;
    color: var(--blue); font-size: 52px; }
  .cover-title { position: absolute; right: 20px; top: 612px; text-align: right;
    font-size: 39px; line-height: 1.12; }
  .cover-band { position: absolute; left: 0; bottom: 0; width: 380px; height: 68px; background: var(--blue);
    display: flex; align-items: center; gap: 14px; padding-left: 18px;
    font-family: "Open Sans", Arial, sans-serif; color: #fff; font-size: 18px; text-transform: uppercase; }
  .band-square { width: 26px; height: 26px; border: 2px solid #fff; }
</style>
</head>
<body>
<div class="brochure">
  <svg class="brochure-art" viewBox="0 0 1140 860" width="1140" height="860">
    <defs>
      <linearGradient id="photoTone" x1="0" y1="0" x2="1" y2="0.6">
        <stop offset="0" stop-color="var(--photo-a)"/>
        <stop offset="0.5" stop-color="var(--photo-b)"/>
        <stop offset="1" stop-color="var(--photo-c)"/>
      </linearGradient>
    </defs>
    <!-- inside panel top band -->
    <path d="M0 0 H380 V228 Q190 236 0 242 Z" fill="var(--blue)"/>
    <!-- inside panel divider -->
    <path d="M0 646 Q190 640 380 628" stroke="var(--dark-rule)" stroke-width="3" fill="none"/>
    <path d="M0 652 Q190 646 380 634" stroke="var(--blue)" stroke-width="6" fill="none"/>
    <!-- photo area across back and cover -->
    <path d="M380 0 H1140 V508 Q960 560 760 628 V632 H380 Z" fill="url(#photoTone)"
      role="img" aria-label="Photo of two smiling businessmen in suits reviewing figures on a tablet"/>
    <path d="M380 634 H760" stroke="var(--dark-rule)" stroke-width="3"/>
    <path d="M380 640 H760" stroke="var(--blue)" stroke-width="4"/>
    <path d="M760 632 Q960 566 1140 514" stroke="var(--blue)" stroke-width="7" fill="none"/>
    <path d="M760 640 Q960 576 1140 524" stroke="var(--dark-rule)" stroke-width="2" fill="none"/>
    <path d="M760 792 H1140" stroke="var(--dark-rule)" stroke-width="3"/>
  </svg>

  <section class="panel panel-inside">
    <h2 class="headline">Here to simplify the<br>bookkeeping process.</h2>
    <h3 class="section-title what-title">
      <span class="icon-dot"><svg width="16" height="16" viewBox="0 0 16 16"><circle cx="6" cy="9" r="4" fill="none" stroke="#fff" stroke-width="2"/><circle cx="12" cy="4" r="2.5" fill="none" stroke="#fff" stroke-width="1.6"/></svg></span>
      What we do:
    </h3>
    <p class="about-copy">Allow business owners to spend more time focusing on their core business by providing comprehensive bookkeeping and business consulting services. We provide the financial data and tools that allow businesses to maximize profitability and focus on growth and other areas of their business. We consider our business to be an extension of your business and look forward to the opportunity to exceed your expectations!</p>
    <h3 class="section-title talk-title">
      <span class="icon-dot"><svg width="16" height="16" viewBox="0 0 16 16"><path d="M2 6 H6 L12 2 V14 L6 10 H2 Z" fill="#fff"/></svg></span>
      Let's talk
    </h3>
    <p class="talk-copy">Schedule a no-obligation consultation today</p>
  </section>

  <section class="panel panel-back">
    <ul class="values">
      <li><span class="icon-dot"><svg width="16" height="16" viewBox="0 0 16 16"><path d="M6 10 L10 6 M4.5 8.5 L3 10 A2.5 2.5 0 0 0 6 13 L7.5 11.5 M8.5 4.5 L10 3 A2.5 2.5 0 0 1 13 6 L11.5 7.5" stroke="#fff" stroke-width="2" fill="none" stroke-linecap="round"/></svg></span>Trustworthy</li>
      <li><span class="icon-dot"><svg width="16" height="16" viewBox="0 0 16 16"><rect x="2" y="10" width="2.5" height="4" fill="#fff"/><rect x="6" y="7" width="2.5" height="7" fill="#fff"/><rect x="10" y="3" width="2.5" height="11" fill="#fff"/></svg></span>Experienced</li>
      <li><span class="icon-dot"><svg width="16" height="16" viewBox="0 0 16 16"><path d="M8 1.5 L13.5 3.5 V8 Q13.5 12.5 8 14.5 Q2.5 12.5 2.5 8 V3.5 Z" fill="none" stroke="#fff" stroke-width="1.8"/></svg></span>Reliable</li>
    </ul>
    <address class="contact" style="font-style:normal">
      <p class="contact-title">Contact Us.</p>
      <p>Phone: 555.014.0277</p>
      <p>Email: mara@halvorineledgers.com</p>
      <p>Web: www.halvorineledgers.com</p>
    </address>
    <p class="back-brand">HL&amp;A</p>
    <p class="back-address">Halvorine Ledgers &amp;<br>Advisory<br>Marrow Valley, PA</p>
  </section>

  <section class="panel panel-cover">
    <div class="cover-mark">HL&amp;A</div>
    <h1 class="cover-title">Expert<br>bookkeeping<br>services for<br>small businesses</h1>
    <div class="cover-band"><span class="band-square"></span>Halvorine Ledgers &amp; Advisory</div>
  </section>
</div>
</body>
</html>
```